Non-Profit focusing on clean water needs a poster/flyer design for our annual Stroll 2 Shore

We need a poster and flyer design for our annual Stroll 2 Shore event which will be held on Saturday, March 21st (Shared River Day) at Morrow Fern Green.

HEAD:

Think Globally, Walk Locally.

SUB:

Join K7L in Santa Barbara on Shared River Day for a Stroll 2 Shore.

PHOTOS:

(one photo of past walk – crowd scene but with one face standing out – smaller photos of our team working out of country)

SUB:

Saturday, March 21st, 10am - 2pm

HEAD

Morrow Fern Green, Santa Barbara

COPY:

For more info check out our website: www.kindrowcircle.org, or contact our Director: dana@kindrowcircle.org; 805 312 4896

K7L Logo with Tag Line

NOTHING ELSE.

The final design should communicate fun for the whole family. Blue-ish shades to denote water. Be the generation that solves the world's water crisis.

Also, no need to use the attached photos if you can come up with a cool big idea graphic.

```html
<!DOCTYPE html>
<html lang="en">
<head>
<meta charset="utf-8">
<title>Stroll 2 Shore – Poster</title>
<link rel="stylesheet" href="https://fonts.googleapis.com/css2?family=Baumans&family=Archivo+Narrow:wght@400;600;700&display=swap">
<style>
  :root {
    --page-bg: #e9e9e7;
    --poster-top: #e2edf8;
    --poster-mid: #f5f9fd;
    --ink: #111111;
    --royal: #2a3aa8;
    --violet: #4a3f9c;
    --sky: #1e9fd6;
    --cyan: #2bb3e6;
    --art-light: #cfe3f6;
    --art-mid: #5e9fe0;
    --art-deep: #2453b0;
    --white: #ffffff;
  }
  * { margin: 0; padding: 0; box-sizing: border-box; }
  html, body { width: 1200px; height: 1148px; overflow: hidden; }
  body { background: var(--page-bg); position: relative; }

  .poster {
    position: absolute;
    left: 250px; top: 20px;
    width: 700px; height: 1108px;
    background: linear-gradient(180deg, var(--poster-top) 0%, var(--poster-mid) 45%, var(--white) 100%);
    overflow: hidden;
  }

  .headline {
    position: absolute; left: 70px; top: 58px;
    font-family: "Baumans", "Comfortaa", sans-serif;
    font-weight: 400;
    font-size: 70px; line-height: 57px;
    letter-spacing: 3px;
    text-transform: uppercase;
  }
  .headline span {
    display: block;
    background: linear-gradient(180deg, var(--cyan) 0%, var(--royal) 55%, var(--violet) 100%);
    -webkit-background-clip: text; background-clip: text;
    color: transparent;
  }

  .intro {
    position: absolute; left: 70px; top: 304px;
    font-family: "Archivo Narrow", "Arial Narrow", sans-serif;
    font-weight: 700; font-size: 21px; line-height: 28px;
    color: var(--ink); text-transform: uppercase;
  }

  .event-name {
    position: absolute; left: 70px; top: 412px;
    font-family: "Baumans", "Comfortaa", sans-serif;
    font-weight: 400;
    font-size: 68px; line-height: 62px;
    text-transform: uppercase; letter-spacing: 1px;
    background: linear-gradient(180deg, var(--cyan) 0%, var(--royal) 60%, var(--violet) 100%);
    -webkit-background-clip: text; background-clip: text;
    color: transparent;
  }
  .event-name .num { font-size: 40px; vertical-align: top; }

  .detail {
    position: absolute; left: 70px;
    font-family: "Archivo Narrow", "Arial Narrow", sans-serif;
    white-space: nowrap;
  }
  .detail-when { color: var(--sky); font-weight: 600; font-size: 24px; line-height: 28px; }
  .detail-where { color: var(--ink); font-weight: 700; font-size: 23px; line-height: 24px; text-transform: uppercase; }
  .detail-note { color: var(--cyan); font-weight: 400; font-size: 16px; line-height: 20px; text-transform: uppercase; }
  .detail-link { color: var(--sky); font-weight: 600; font-size: 19px; line-height: 22px; text-transform: uppercase; }

  .footprint-art {
    position: absolute; left: 500px; top: 66px;
    width: 190px; height: 906px;
    border-radius: 90px 90px 80px 80px / 160px 160px 110px 110px;
    background: radial-gradient(ellipse 70% 60% at 50% 40%, var(--art-mid) 0%, var(--art-light) 100%);
    opacity: 0.55;
  }

  .brand {
    position: absolute; left: 136px; top: 844px;
    width: 180px; height: 192px; border-radius: 50%;
    background: var(--ink);
    display: flex; align-items: center; justify-content: center;
  }
  .brand-name {
    font-family: "Archivo Narrow", "Arial Narrow", sans-serif;
    font-weight: 700; font-size: 54px; color: var(--white);
  }
  .tagline {
    position: absolute; left: 340px; top: 940px;
    font-family: "Archivo Narrow", "Arial Narrow", sans-serif;
    font-size: 15px; color: var(--ink);
  }
</style>
</head>
<body>
  <main class="poster">
    <h1 class="headline">
      <span>Think</span>
      <span>Globally</span>
      <span>Walk</span>
      <span>Locally</span>
    </h1>

    <p class="intro">Join K7L in<br>Santa Barbara on<br>Shared River Day<br>for a</p>

    <h2 class="event-name">Stroll<span class="num">2</span><br>Shore</h2>

    <p class="detail detail-when" style="top:554px">SATURDAY, MARCH 21ST,</p>
    <p class="detail detail-when" style="top:582px">10am - 2pm</p>
    <p class="detail detail-where" style="top:612px">Morrow Fern Green,</p>
    <p class="detail detail-where" style="top:636px">Santa Barbara</p>
    <p class="detail detail-note" style="top:666px">For more info check out our website:</p>
    <p class="detail detail-link" style="top:692px">www.kindrowcircle.org,</p>
    <p class="detail detail-note" style="top:724px">or contact our director:</p>
    <p class="detail detail-link" style="top:756px">dana@kindrowcircle.org;</p>
    <p class="detail detail-link" style="top:792px">805 312 4896</p>

    <div class="footprint-art" role="img" aria-label="Illustration of a bare footprint built from many blue globe-shaped water droplets"></div>

    <div class="brand"><span class="brand-name">K7L</span></div>
    <p class="tagline">A Movement of Young People</p>
  </main>
</body>
</html>
```